UX Design Document Management App Project

UPDATED PROJECT and INCREASED TOTAL COST. Also added a new design guideline document (4QK - Concept - The Lantern 170613.pdf).

We are a small start-up company based in Sydney, Australia. We have the ideas and coding skills to have built a revolutionary document management app that helps knowledge workers deal with information overload.

We are about to launch an alpha version of a document management app on the iPhone. We have created a series of screens but they lack the brilliance that only a talented graphic designer can deliver. So we would like to find a design partner who can make a contribution in two areas:

1. Make specific changes to our screens such as formatting images so they better blend into the background.
2. Examine our overall UX and either suggest changes or propose new design concepts.
3. Create a logo for this product.

We have completed a pretty comprehensive design brief that we attach to this project and also a set of our existing screen designs in a mix of Photoshop and Keynote formats that we can share with you.

Once we have launched are alpha product, we hope that the winner of this project (our future graphic design partner) will work with us on another project that aims to radically improve the UX of our app in time for a full version 1.0 launch later this year.

We'd like to lock-down the alpha UX in 5 to 10 days but if the ideas you have are exciting enough we can extend this time.
Updates

Project now has a SIGNIFICANTLY INCREASED BUDGET (almost doubled) and an expanded scope to deliver a logo for our product. Check out the additional design brief document just uploaded.

Hello Designers,

Just to let you know that we have updated the project and INCREASED THE TOTAL BUDGET. We have also added a new design guideline document (4QK - Concept - The Lantern 170613.pdf) to help inspire you!

The project now has a significantly increased budget (almost doubled) and an expanded scope to also deliver a logo for our Mollant product. Check out the additional design brief document just uploaded.

Thanks for participating!

All the best,

Gareth

Barring any unforeseen circumstances, this design competition will remain open until midnight Pacific Standard Time this Sunday. That means about 10 am Sydney time this Monday, July 1st. Good luck and get your designs in!

Project Deadline Extended
Reason: I agreed to use PST not AEST!

Target Market(s)

individual knowledge workers: professionals, office workers/managers, university students, academics/researchers, etc.

Industry/Entity Type

Graphic Designer

Requirements
Must have
• professional, highly effective UX

```html
<!DOCTYPE html>
<html lang="en">
<head>
<meta charset="utf-8">
<title>Mollant – Semantic Cloud screens</title>
<link rel="stylesheet" href="https://fonts.googleapis.com/css2?family=Mada:wght@300;400&display=swap">
<style>
:root{
  --canvas:#e6e6e8;
  --teal:#0ea99a;
  --white:#ffffff;
  --body-top:#ffffff;
  --body-bottom:#f0f0f0;
  --rule:#dcdcdc;
  --text-grey:#6e6e6e;
  --text-dark:#222222;
  --date-red:#e07070;
  --footer-grey:#909092;
  --slider-line:#8c8c8c;
  --w-red:#d9442e;
  --w-blue:#29a8e0;
  --w-purple:#a03090;
  --w-pink:#d9587f;
  --w-steel:#3a7fa8;
  --w-olive:#9fa050;
  --w-black:#111111;
  --w-magenta:#c05cc0;
  --w-yellow:#e0c050;
}
*{margin:0;padding:0;box-sizing:border-box}
html,body{width:1200px;height:1063px;overflow:hidden;background:var(--canvas);font-family:"Mada",sans-serif;font-weight:300}
.board{position:relative;width:1200px;height:1063px}
.screen{position:absolute;top:35px;width:487px;height:741px;background:linear-gradient(var(--body-top) 45%,var(--body-bottom));overflow:hidden}
.screen--small{left:28px}
.screen--large{left:597px}
.app-bar{position:absolute;left:0;top:0;width:100%;height:82px;background:var(--teal)}
.app-bar__icon{position:absolute;top:17px;width:48px;height:48px}
.app-bar__back{left:17px}
.app-bar__settings{left:427px}
.app-bar__title{position:absolute;left:0;width:100%;top:22px;text-align:center;color:var(--white);font-size:30px;font-weight:400}
.intro{position:absolute;left:0;width:100%;top:98px;text-align:center;color:var(--text-grey);font-size:21px;line-height:28px}
.rule{position:absolute;left:19px;width:453px;height:3px;background:var(--rule)}
.rule--top{top:179px}
.rule--bottom{top:267px}
.doc{position:absolute;left:20px;top:190px;height:68px}
.doc__date{position:absolute;left:0;top:0;width:68px;height:68px;border-radius:50%;background:var(--date-red);color:var(--white);text-align:center}
.doc__day{display:block;font-size:34px;line-height:34px;padding-top:9px}
.doc__month{display:block;font-size:13px;line-height:13px}
.doc__name{position:absolute;left:90px;top:15px;white-space:nowrap;font-size:21px;font-weight:400;color:var(--text-dark)}
.doc__summary{position:absolute;left:90px;top:41px;white-space:nowrap;font-size:12px;color:var(--text-grey)}
.cloud__word{position:absolute;transform:translate(-50%,-50%);white-space:nowrap;line-height:1}
.w-shopping{left:244px;top:339px;font-size:30px;color:var(--w-red)}
.w-healthy{left:139px;top:376px;font-size:42px;color:var(--w-blue)}
.w-lorem{left:338px;top:381px;font-size:28px;color:var(--w-purple)}
.w-organic{left:224px;top:455px;font-size:30px;color:var(--w-pink)}
.w-food{left:266px;top:549px;font-size:54px;color:var(--w-blue)}
.w-ipsum{left:162px;top:420px;font-size:30px;color:var(--w-steel)}
.w-amet{left:255px;top:410px;font-size:28px;color:var(--w-olive)}
.w-sit{left:334px;top:421px;font-size:28px;color:var(--w-black)}
.w-vegetable{left:167px;top:498px;font-size:30px;color:var(--w-magenta)}
.w-dolor{left:290px;top:490px;font-size:30px;color:var(--w-yellow)}
.screen--large .w-organic{left:225px;top:454px}
.slider{position:absolute;left:9px;top:655px;width:454px;height:3px;background:var(--slider-line)}
.slider__knob{position:absolute;top:-15px;width:33px;height:33px;border-radius:50%;background:var(--teal);border:3px solid var(--white);box-shadow:0 0 0 1px #cfcfcf}
.screen--small .slider__knob{left:94px}
.screen--large .slider__knob{left:315px}
.slider__hint{position:absolute;left:0;width:100%;top:677px;text-align:center;color:var(--text-grey);font-size:21px}
.footer{position:absolute;left:0;bottom:0;width:100%;height:27px;background:var(--footer-grey)}
.footer__handle{position:absolute;left:224px;top:7px;width:38px;height:14px}
.notes{position:absolute;left:54px;top:845px;color:var(--text-dark);font-size:31px;line-height:42px;font-weight:300}
</style>
</head>
<body>
<div class="board">

  <section class="screen screen--small">
    <header class="app-bar">
      <svg class="app-bar__icon app-bar__back" viewBox="0 0 48 48"><circle cx="24" cy="24" r="21" fill="none" stroke="#fff" stroke-width="3.5"/><path d="M34 24H15M23 15l-9 9 9 9" fill="none" stroke="#fff" stroke-width="4.5" stroke-linecap="round" stroke-linejoin="round"/></svg>
      <h1 class="app-bar__title">Mollant</h1>
      <svg class="app-bar__icon app-bar__settings" viewBox="0 0 48 48"><circle cx="24" cy="24" r="21" fill="none" stroke="#fff" stroke-width="3.5"/><g fill="#fff"><circle cx="24" cy="24" r="10"/><rect x="21" y="9" width="6" height="30" rx="1"/><rect x="21" y="9" width="6" height="30" rx="1" transform="rotate(45 24 24)"/><rect x="21" y="9" width="6" height="30" rx="1" transform="rotate(90 24 24)"/><rect x="21" y="9" width="6" height="30" rx="1" transform="rotate(135 24 24)"/></g><circle cx="24" cy="24" r="4.5" fill="var(--teal)"/></svg>
    </header>
    <p class="intro">Semantic Cloud gives you a very<br>quick glance at the document.</p>
    <div class="rule rule--top"></div>
    <div class="doc">
      <div class="doc__date"><span class="doc__day">03</span><span class="doc__month">May</span></div>
      <div class="doc__name">Document Name</div>
      <div class="doc__summary">Lorem ipsum dolor sit amet and</div>
    </div>
    <div class="rule rule--bottom"></div>
    <div class="cloud">
      <span class="cloud__word w-shopping">Shopping</span>
      <span class="cloud__word w-healthy">Healthy</span>
      <span class="cloud__word w-lorem">Lorem</span>
      <span class="cloud__word w-organic">Organic</span>
      <span class="cloud__word w-food">Food</span>
    </div>
    <div class="slider"><span class="slider__knob"></span></div>
    <p class="slider__hint">slide here to add more words</p>
    <footer class="footer"><svg class="footer__handle" viewBox="0 0 38 14"><g stroke="#fff" stroke-width="1.6"><line x1="0" y1="2" x2="38" y2="2"/><line x1="0" y1="5.5" x2="38" y2="5.5"/><line x1="0" y1="9" x2="38" y2="9"/><line x1="0" y1="12.5" x2="38" y2="12.5"/></g></svg></footer>
  </section>

  <section class="screen screen--large">
    <header class="app-bar">
      <svg class="app-bar__icon app-bar__back" viewBox="0 0 48 48"><circle cx="24" cy="24" r="21" fill="none" stroke="#fff" stroke-width="3.5"/><path d="M34 24H15M23 15l-9 9 9 9" fill="none" stroke="#fff" stroke-width="4.5" stroke-linecap="round" stroke-linejoin="round"/></svg>
      <h1 class="app-bar__title">Mollant</h1>
      <svg class="app-bar__icon app-bar__settings" viewBox="0 0 48 48"><circle cx="24" cy="24" r="21" fill="none" stroke="#fff" stroke-width="3.5"/><g fill="#fff"><circle cx="24" cy="24" r="10"/><rect x="21" y="9" width="6" height="30" rx="1"/><rect x="21" y="9" width="6" height="30" rx="1" transform="rotate(45 24 24)"/><rect x="21" y="9" width="6" height="30" rx="1" transform="rotate(90 24 24)"/><rect x="21" y="9" width="6" height="30" rx="1" transform="rotate(135 24 24)"/></g><circle cx="24" cy="24" r="4.5" fill="var(--teal)"/></svg>
    </header>
    <p class="intro">Semantic Cloud gives you a very<br>quick glance at the document.</p>
    <div class="rule rule--top"></div>
    <div class="doc">
      <div class="doc__date"><span class="doc__day">03</span><span class="doc__month">May</span></div>
      <div class="doc__name">Document Name</div>
      <div class="doc__summary">Lorem ipsum dolor sit amet and</div>
    </div>
    <div class="rule rule--bottom"></div>
    <div class="cloud">
      <span class="cloud__word w-shopping">Shopping</span>
      <span class="cloud__word w-healthy">Healthy</span>
      <span class="cloud__word w-lorem">Lorem</span>
      <span class="cloud__word w-ipsum">ipsum</span>
      <span class="cloud__word w-amet">amet</span>
      <span class="cloud__word w-sit">sit</span>
      <span class="cloud__word w-organic">Organic</span>
      <span class="cloud__word w-vegetable">Vegetable</span>
      <span class="cloud__word w-dolor">dolor</span>
      <span class="cloud__word w-food">Food</span>
    </div>
    <div class="slider"><span class="slider__knob"></span></div>
    <p class="slider__hint">slide here to add more words</p>
    <footer class="footer"><svg class="footer__handle" viewBox="0 0 38 14"><g stroke="#fff" stroke-width="1.6"><line x1="0" y1="2" x2="38" y2="2"/><line x1="0" y1="5.5" x2="38" y2="5.5"/><line x1="0" y1="9" x2="38" y2="9"/><line x1="0" y1="12.5" x2="38" y2="12.5"/></g></svg></footer>
  </section>

  <p class="notes">Suggestions;<br>1. Word cloud can be small with few words or else larger with some more words<br>(The larger version is processed but it is only showed whrn the user slides the<br>scrol to the right side.)</p>

</div>
</body>
</html>
```